ambitious event and festival agency from austria needs fresh business card design

A new design is due for the new headquarters and the new challenges. We organize events for different target groups from 16 to 60 years. The design should therefore be straightforward and not confused, so we are open to new colors and the logo may also be changed. In general, however, the most interesting suggestions are the most interesting ones. after this order we are looking for more graphics for partyvelt facebook instagramm homepage etc A new design is due for the new headquarters and the new challenges. We organize events for different target groups from 16 to 60 years. The design should therefore be straightforward and not confused, so we are open to new colors and the logo may also be changed. In general, however, the most interesting suggestions are the most interesting ones. after this order we are looking for more graphics for partyvelt facebook instagramm homepage etc A new design is due for the new headquarters and the new challenges. We organize events for different target groups from 16 to 60 years. The design should therefore be straightforward and not confused, so we are open to new colors and the logo may also be changed. In general, however, the most interesting suggestions are the most interesting ones. after this order we are looking for more graphics for partyvelt facebook instagramm homepage etc

Reason: I am sorry for this decision but i need some more time. No new designs please, there are so many good ones and I will have made a decision in the next 3 days.

Target Market(s)

Industry/Entity Type

Business

Font styles to use
Serif
Sans Serif

Colors

Designer to choose colors to be used in the design.

Requirements
Must have
Nice to have
Should not have

```html
<!DOCTYPE html>
<html lang="en">
<head>
<meta charset="utf-8">
<title>partyvelt business card</title>
<link href="https://fonts.googleapis.com/css2?family=Oswald:wght@500&family=Work+Sans:ital,wght@0,300;0,400;0,500;1,300&display=swap" rel="stylesheet">
<style>
  :root {
    --bg: #1c1c1e;
    --red: #a51f35;
    --red-light: #b84a5a;
    --red-dark: #9e1a30;
    --white: #ffffff;
    --grey: #6b6b6b;
    --grey-light: #9a9a9a;
  }
  * { box-sizing: border-box; margin: 0; padding: 0; }
  html, body { width: 1200px; height: 900px; overflow: hidden; }
  body {
    background: var(--bg);
    font-family: "Work Sans", sans-serif;
    display: flex;
    flex-direction: column;
    align-items: center;
    justify-content: center;
    gap: 40px;
  }
  .card {
    width: 640px;
    height: 384px;
    border-radius: 22px;
    overflow: hidden;
    position: relative;
  }
  .card-back {
    background: linear-gradient(100deg, var(--red-light) 0%, var(--red) 55%, var(--red-dark) 100%);
    display: flex;
    align-items: center;
    justify-content: center;
  }
  .wordmark {
    font-family: "Work Sans", sans-serif;
    font-weight: 500;
    letter-spacing: 0.5px;
  }
  .card-back .wordmark {
    color: var(--white);
    font-size: 66px;
  }
  .card-front { background: var(--white); }
  .card-front .wordmark {
    position: absolute;
    top: 30px;
    right: 40px;
    color: var(--red);
    font-size: 44px;
  }
  .holder {
    position: absolute;
    left: 44px;
    top: 146px;
  }
  .holder-name {
    font-family: "Oswald", sans-serif;
    font-weight: 500;
    font-size: 25px;
    color: var(--red);
    letter-spacing: 0.3px;
    text-transform: uppercase;
    line-height: 1.1;
  }
  .holder-role {
    font-weight: 300;
    font-style: italic;
    font-size: 17px;
    color: var(--grey-light);
  }
  .divider {
    position: absolute;
    left: 0; right: 0;
    top: 218px;
    height: 4px;
    background: var(--grey);
  }
  .contact-band {
    position: absolute;
    left: 0; right: 0; bottom: 0;
    top: 226px;
    background: linear-gradient(100deg, var(--red-light) 0%, var(--red) 55%, var(--red-dark) 100%);
    color: var(--white);
    padding: 20px 40px 20px 40px;
    display: flex;
    justify-content: space-between;
    align-items: flex-end;
  }
  .contact-list {
    list-style: none;
    align-self: flex-start;
    font-size: 17px;
    font-weight: 400;
    line-height: 1.35;
  }
  .contact-list li { display: flex; align-items: center; gap: 12px; }
  .contact-list svg { width: 12px; height: 12px; flex: none; }
  .address {
    font-style: normal;
    text-align: right;
    font-size: 18px;
    line-height: 1.3;
  }
</style>
</head>
<body>
  <section class="card card-back">
    <span class="wordmark">partyvelt</span>
  </section>

  <section class="card card-front">
    <span class="wordmark">partyvelt</span>
    <div class="holder">
      <p class="holder-name">Markus Feldhofer</p>
      <p class="holder-role">Manager</p>
    </div>
    <div class="divider"></div>
    <div class="contact-band">
      <ul class="contact-list">
        <li>
          <svg viewBox="0 0 12 12"><rect x="3" y="0.5" width="6" height="11" rx="1" fill="none" stroke="#fff" stroke-width="1.2"/><circle cx="6" cy="9.5" r="0.7" fill="#fff"/></svg>
          + 43 660 418 372 5
        </li>
        <li>
          <svg viewBox="0 0 12 12"><rect x="0.6" y="2.5" width="10.8" height="7" fill="none" stroke="#fff" stroke-width="1.2"/><path d="M0.6 2.5 L6 6.5 L11.4 2.5" fill="none" stroke="#fff" stroke-width="1.2"/></svg>
          m.feldhofer@partyvelt.eu
        </li>
        <li>
          <svg viewBox="0 0 12 12"><circle cx="6" cy="6" r="5.2" fill="none" stroke="#fff" stroke-width="1.1"/><ellipse cx="6" cy="6" rx="2.3" ry="5.2" fill="none" stroke="#fff" stroke-width="1"/><path d="M0.8 6 H11.2" stroke="#fff" stroke-width="1"/></svg>
          www.partyvelt.eu
        </li>
      </ul>
      <address class="address">
        partyvelt<br>
        Lindenweg 12<br>
        A4600 Wels
      </address>
    </div>
  </section>
</body>
</html>
```